2 Flyers of Company Core Values/Mission Statement & Who We Are

We are a construction company that needs two flyers for our core values/mission statement and Who We Are. We want something unique and a little edgy.

Flyer 1 will consist of our core values and mission statement below (chart or graphics style would be good). We don't want just wording.

I. Core Values
a. Respect for all people
b. Open, honest, proactive, and energetic two-way communication
c. Our word is our promise
d. Invest in our team members to provide them opportunities for development and advancement
e. Foster an atmosphere that encourages innovation and continuous improvement
f. Sustain a safety-focused culture

J. Core Value Statement
Mission Statement: Halvern Construction is an ever-advancing Christian principled company guided by the core values of respect, proactive two-way communication, keeping promises, investing in people, and innovation. Accordingly, we are committed to excellence in everything we do.

Flyer 2 will consists of a page of "Who We Are" to contain the following information:

A. Strengths/Core Competencies
a. Loyal to employees
b. Honest and fair with employees and customers
c. High-quality work
d. Adaptable to changing market conditions
e. Employees: talented workers, superintendents, and project managers
f. Embrace and adapt to changing technology
B. Mindshare (words we own)
a. Difficult projects (in each sector we serve)
C. What (Product & Service)
a. Timely and successful construction project completion
D. Brand Promise
a. 90% of our customers would do business with us again
b. We treat each customer's project like it was our own investment
E. Brand Promise Guarantee
a. We are a Christian principled company and never compromise our integrity. We are committed to excellence in everything we do.
F. One Phase Strategy (Key to making Money)
a. Understand the markets we serve and manage our people to efficiently serve the customer
G. Differentiating Factors
a. Access to a flexible source of high-quality, on-demand labor
b. More professional than small competitors
c. Big enough to handle the most difficult tasks but small enough to have a personal relationship with the customer
d. Zero-item punch list at project completion
H. X-Factor
a. Access to a flexible source of high-quality, dedicated & talented labor force not available to competitors
J. Purpose
a. Our goal is to improve the quality of life in the communities we serve through constructing great and successful projects.

Construction

```html
<!DOCTYPE html>
<html lang="en">
<head>
<meta charset="utf-8">
<title>Halvern Construction — Core Values</title>
<link rel="stylesheet" href="https://fonts.googleapis.com/css2?family=Fjalla+One&family=Open+Sans:wght@400;700&display=swap">
<style>
  :root {
    --page-bg: #e9ecee;
    --sky: #d6ecf2;
    --ground: #9bd2d5;
    --teal: #12ae96;
    --green: #8dc21f;
    --orange: #f39200;
    --yellow: #f6c800;
    --blue: #0d76bc;
    --magenta: #e4007c;
    --purple: #932283;
    --brown: #b05300;
    --ink: #2b2b2b;
    --white: #ffffff;
  }
  * { box-sizing: border-box; margin: 0; padding: 0; }
  html, body { width: 1041px; height: 1200px; overflow: hidden; background: var(--page-bg); }
  .flyer {
    position: absolute; left: 95px; top: 0; width: 851px; height: 1200px; overflow: hidden;
    background: linear-gradient(to bottom, var(--sky) 0, var(--sky) 700px, var(--ground) 700px);
    font-family: "Open Sans", sans-serif;
  }
  .scene-art {
    position: absolute; left: 0; top: 133px; width: 470px; height: 772px;
    background: linear-gradient(to bottom, #d6ecf2 0%, #a9d2e3 45%, #5b9ec4 70%, #9bd2d5 82%);
  }
  .values-title {
    position: absolute; left: 0; top: 53px; width: 409px; height: 80px;
    background: var(--teal);
    clip-path: polygon(0 0, 380px 0, 409px 40px, 380px 80px, 0 80px);
    color: var(--white); font-family: "Fjalla One", sans-serif; font-size: 60px; line-height: 80px;
    padding-left: 44px; letter-spacing: 0.5px;
  }
  .value-panels { position: absolute; left: 0; top: 0; width: 851px; height: 920px; }
  .value-text {
    position: absolute; left: 576px; width: 268px; height: 142px;
    display: flex; align-items: center;
    color: var(--white); font-weight: 700; font-size: 16.5px; line-height: 23px;
  }
  .mission-title {
    position: absolute; left: 136px; top: 958px; width: 578px; height: 69px;
    background: var(--brown);
    clip-path: polygon(26px 0, 100% 0, 552px 100%, 0 100%);
    border-radius: 10px;
    color: var(--white); font-family: "Fjalla One", sans-serif; font-size: 46px; line-height: 69px; text-align: center;
  }
  .mission-shadow {
    position: absolute; left: 200px; top: 1024px; width: 450px; height: 14px;
    background: radial-gradient(ellipse at center, rgba(0,0,0,0.35), rgba(0,0,0,0) 70%);
  }
  .mission-text {
    position: absolute; left: 65px; top: 1054px; width: 730px;
    color: var(--ink); font-size: 16.2px; line-height: 23.5px;
  }
  .color-bar { position: absolute; left: 0; bottom: 0; width: 851px; height: 20px; display: flex; }
  .color-bar span { flex: 1; }
</style>
</head>
<body>
<main class="flyer">
  <div class="scene-art" role="img" aria-label="Illustration of a businessman with a briefcase waving in front of a city skyline"></div>

  <h1 class="values-title">Core Values</h1>

  <svg class="value-panels" viewBox="0 0 851 920" aria-hidden="true">
    <defs>
      <filter id="panel-shadow" x="-5%" y="-10%" width="110%" height="130%">
        <feDropShadow dx="0" dy="3" stdDeviation="3" flood-color="#000" flood-opacity="0.25"/>
      </filter>
    </defs>
    <g filter="url(#panel-shadow)">
      <path fill="var(--green)"   d="M434 53 H851 V195 H478 L420 75 Q414 53 434 53Z"/>
      <path fill="var(--orange)"  d="M434 195 H851 V337 H478 L420 217 Q414 195 434 195Z"/>
      <path fill="var(--yellow)"  d="M434 337 H851 V479 H478 L420 359 Q414 337 434 337Z"/>
      <path fill="var(--blue)"    d="M434 479 H851 V621 H478 L420 501 Q414 479 434 479Z"/>
      <path fill="var(--magenta)" d="M434 621 H851 V763 H478 L420 643 Q414 621 434 621Z"/>
      <path fill="var(--purple)"  d="M434 763 H851 V905 H478 L420 785 Q414 763 434 763Z"/>
    </g>
    <g fill="var(--white)">
      <!-- group of people -->
      <circle cx="517" cy="100" r="9"/><circle cx="497" cy="108" r="7"/><circle cx="537" cy="108" r="7"/>
      <circle cx="481" cy="116" r="6"/><circle cx="553" cy="116" r="6"/>
      <rect x="505" y="111" width="24" height="33" rx="8"/>
      <rect x="487" y="117" width="19" height="24" rx="7"/><rect x="528" y="117" width="19" height="24" rx="7"/>
      <rect x="473" y="124" width="15" height="18" rx="6"/><rect x="546" y="124" width="15" height="18" rx="6"/>
      <!-- conversation -->
      <path d="M498 228 h34 a8 8 0 0 1 8 8 v10 a8 8 0 0 1 -8 8 h-18 l-8 7 v-7 h-8 a8 8 0 0 1 -8 -8 v-10 a8 8 0 0 1 8 -8z"/>
      <circle cx="501" cy="270" r="7"/><circle cx="532" cy="270" r="7"/>
      <rect x="491" y="279" width="20" height="26" rx="6"/><rect x="522" y="279" width="20" height="26" rx="6"/>
      <!-- handshake -->
      <path d="M478 396 l14 -14 l18 8 l16 -6 l18 8 l14 -10 l6 22 l-10 6 l-20 20 q-6 5 -12 0 l-22 -16 l-14 6z"/>
      <!-- team celebrating -->
      <circle cx="497" cy="530" r="6"/><circle cx="517" cy="526" r="7"/><circle cx="537" cy="530" r="6"/>
      <rect x="490" y="538" width="14" height="44" rx="5"/><rect x="509" y="535" width="16" height="48" rx="5"/><rect x="530" y="538" width="14" height="44" rx="5"/>
      <rect x="484" y="512" width="5" height="26" rx="2" transform="rotate(-12 486 525)"/>
      <rect x="545" y="512" width="5" height="26" rx="2" transform="rotate(12 547 525)"/>
      <!-- plant in hand -->
      <path d="M515 700 q-2 -20 -22 -28 q2 22 22 28z"/><path d="M519 698 q4 -24 28 -30 q-4 26 -28 30z"/>
      <rect x="515" y="695" width="4" height="18"/>
      <path d="M480 704 h12 v26 h-12z M494 712 h20 q8 0 8 6 h20 q10 0 14 -8 l6 4 q-6 18 -24 20 h-44z"/>
      <!-- recycle -->
      <path d="M517 810 l14 22 h-9 l-5 -8 l-10 16 l-9 -5z M548 846 l-10 18 h-24 v9 l-14 -14 l14 -14 v9 h19 l7 -12z M486 846 l9 -4 l-12 -20 l8 -4 l-20 2 l-3 20 l8 -5z" />
    </g>
  </svg>

  <p class="value-text" style="top:53px">Respect for all people</p>
  <p class="value-text" style="top:195px">Open, honest, proactive, and energetic two-way communication</p>
  <p class="value-text" style="top:337px">Our word is our promise</p>
  <p class="value-text" style="top:479px">Invest in our team members to provide them opportunities for development and advancement</p>
  <p class="value-text" style="top:621px">Foster an atmosphere that encourages innovation and continuous improvement</p>
  <p class="value-text" style="top:763px">Sustain a safety-focused culture</p>

  <div class="mission-shadow"></div>
  <h2 class="mission-title">Mission Statement</h2>
  <p class="mission-text">Halvern Construction is an ever-advancing Christian principled company guided by the core values of respect, proactive two-way communication, keeping promises, investing in people, and innovation. Accordingly, we are committed to excellence in everything we do.</p>

  <div class="color-bar">
    <span style="background:var(--green)"></span><span style="background:var(--orange)"></span>
    <span style="background:var(--yellow)"></span><span style="background:var(--blue)"></span>
    <span style="background:var(--magenta)"></span><span style="background:var(--purple)"></span>
  </div>
</main>
</body>
</html>
```